A-Stand Directional Sign Design

Objective:
We need a professional graphic design for an A-Stand sign that will guide customers arriving in our parking lot to our office. The design should be visually clear, welcoming, and aligned with our brand identity.
REQUIREMENTS:
Two versions of the design:
- One with an arrow pointing left
- One with an arrow pointing right
(This allows us to place the A-Stand anywhere and flip the graphic as needed.)
DIMENSIONS:
- Viewable Area: 30" x 40"
BRAND ALIGNMENT:
- Colors, fonts, and overall style should match our website: www.glidecrest.com
- Clean, modern, and professional look consistent with our aviation/tourism brand
CONTENT:
- Clear directional arrow (left or right depending on version)
- Text: “Office Entrance” or similar concise wording (designers may propose alternatives if they improve clarity)
READABILITY:
- Bold, high-contrast design for visibility from a distance
- Simple layout that avoids clutter
DELIVERABLES:
- Final artwork in print-ready format (PDF preferred)
- Two versions: Arrow Left and Arrow Right
DESIGN GOAL:
Ensure customers can easily find our office upon arrival, while reinforcing glideCREST’s professional and welcoming brand image.
Target Market(s)
Tourism
Look and feel

```html
<!DOCTYPE html>
<html lang="en">
<head>
<meta charset="UTF-8">
<title>glideCREST – Office Entrance Sign</title>
<link href="https://fonts.googleapis.com/css2?family=Montserrat:wght@600;700&display=swap" rel="stylesheet">
<style>
  :root {
    --brand-blue: #0868F6;
    --white: #FFFFFF;
  }
  * { margin: 0; padding: 0; box-sizing: border-box; }
  html, body {
    width: 900px;
    height: 1200px;
    overflow: hidden;
    background: var(--white);
  }
  .sign {
    position: relative;
    width: 900px;
    height: 1200px;
    font-family: "Montserrat", sans-serif;
    color: var(--white);
  }
  .band-top {
    position: absolute;
    left: 0; top: 0;
    width: 900px; height: 356px;
    background: var(--brand-blue);
  }
  .band-arrow {
    position: absolute;
    left: 0; top: 356px;
    width: 900px; height: 332px;
    background: var(--white);
  }
  .band-bottom {
    position: absolute;
    left: 0; top: 688px;
    width: 900px; height: 512px;
    background: var(--brand-blue);
  }
  .brand-name {
    position: absolute;
    left: 0; top: 160px;
    width: 900px;
    text-align: center;
    font-weight: 600;
    font-size: 50px;
    line-height: 1;
    letter-spacing: 1px;
    color: var(--white);
  }
  .direction-arrow {
    position: absolute;
    left: 0; top: 0;
    width: 900px; height: 1200px;
  }
  .direction-arrow path { fill: var(--brand-blue); }
  .label {
    position: absolute;
    left: 0;
    width: 900px;
    text-align: center;
    font-weight: 700;
    line-height: 1;
    text-transform: uppercase;
    color: var(--white);
  }
  .label-office {
    top: 796px;
    font-size: 128px;
    letter-spacing: 2px;
  }
  .label-entrance {
    top: 922px;
    font-size: 114px;
    letter-spacing: 2px;
  }
</style>
</head>
<body>
  <main class="sign">
    <section class="band-top">
      <div class="brand-name">glideCREST</div>
    </section>
    <section class="band-arrow"></section>
    <svg class="direction-arrow" viewBox="0 0 900 1200" aria-hidden="true">
      <path d="M155 518 L318 408 Q338 395 350 410 Q355 420 350 434 L340 470 Q339 475 344 475 L713 475 Q745 475 745 507 L745 538 Q745 570 713 570 L342 570 Q336 570 338 576 L350 612 Q357 632 353 636 Q346 652 320 636 Z"/>
    </svg>
    <section class="band-bottom"></section>
    <h1 class="label label-office">Office</h1>
    <h2 class="label label-entrance">Entrance</h2>
  </main>
</body>
</html>
```